Business card design needed

Double sided
Color, unique, elegant

Maybe put this quote somewhere?? But I think it might make it to cluttered?
“The Pilates Method of Body
Conditioning develops the body
uniformly, corrects posture, restores
vitality, invigorates the mind and
elevates the spirit”
- Henrik Dovacombe

Industry/Entity Type

Business

Contact Information for Business Card

Marta Kellbrook
Pilates Instructor & Personal trainer
Mobile: 0498265043
www.lorvix.com.au
email: lorvixhealth.fitness@qentamail.com

```html
<!DOCTYPE html>
<html lang="en">
<head>
<meta charset="utf-8">
<title>Lorvix Health and Fitness – Business Card</title>
<link rel="stylesheet" href="https://fonts.googleapis.com/css2?family=Didact+Gothic&family=Open+Sans:ital,wght@0,700;1,400&display=swap">
<style>
  :root {
    --bg: #ece9e4;
    --card: #ffffff;
    --ink: #1d1d1d;
    --ink-soft: #333333;
    --green: #a6c936;
    --pink: #e5287f;
    --blue: #7fa6d8;
    --purple: #8c2f8e;
    --yellow: #f7e614;
    --orange: #f28c26;
    --logo-pink: #c76fb0;
  }
  * { margin: 0; padding: 0; box-sizing: border-box; }
  html, body { width: 1200px; height: 1045px; overflow: hidden; background: var(--bg); }
  body { position: relative; font-family: "Didact Gothic", sans-serif; color: var(--ink); }

  .card {
    position: absolute; left: 170px; width: 860px; height: 478px;
    background: var(--card); box-shadow: 0 4px 16px rgba(0,0,0,.15);
  }
  .card--contact { top: 30px; }
  .card--feature { top: 537px; }

  /* brand lockup */
  .brand { position: absolute; display: flex; flex-direction: column; align-items: flex-start; }
  .brand__row { display: flex; align-items: center; gap: 14px; }
  .brand__dot { width: 34px; height: 34px; border-radius: 50%; background: var(--logo-pink); }
  .brand__name { font-family: "Didact Gothic", sans-serif; font-size: 60px; letter-spacing: 4px; color: var(--ink-soft); line-height: 1; }
  .brand__tagline { font-size: 22px; margin-top: 8px; margin-left: 48px; color: var(--ink); }
  .card--contact .brand { left: 80px; top: 220px; }
  .card--feature .brand { left: 70px; top: 150px; }

  /* contact side */
  .activity-strip {
    position: absolute; left: 430px; top: 48px; width: 390px; height: 80px;
    background: linear-gradient(90deg, #b99bd6, #8fa7dc, #8fd0c8, #b6d88a, #f2d26b, #f29a7a, #d792c9);
    opacity: .55; border-radius: 4px;
  }
  .contact { position: absolute; right: 40px; top: 145px; text-align: right; }
  .contact__line { display: flex; justify-content: flex-end; align-items: center; gap: 10px; font-size: 21px; line-height: 32px; }
  .contact__name { font-family: "Open Sans", sans-serif; font-weight: 700; font-size: 22px; }
  .contact__key {
    width: 16px; height: 16px; font-size: 10px; line-height: 16px; text-align: center; color: var(--ink);
  }
  .key--green { background: var(--green); }
  .key--pink { background: var(--pink); }
  .key--blue { background: var(--blue); }
  .key--orange { background: var(--orange); }
  .contact__email { position: absolute; right: 66px; top: 318px; font-size: 21px; }

  /* feature side */
  .tile { position: absolute; }
  .tile--green { left: 420px; top: 40px; width: 135px; height: 150px; background: var(--green); }
  .tile--purple { left: 420px; top: 200px; width: 135px; height: 160px; background: var(--purple); }
  .tile--pink { left: 565px; top: 60px; width: 135px; height: 140px; background: var(--pink); }
  .tile--yellow { left: 565px; top: 210px; width: 135px; height: 150px; background: var(--yellow); }
  .tile--blue { left: 710px; top: 90px; width: 130px; height: 135px; background: var(--blue); }
  .tile--orange { left: 710px; top: 235px; width: 130px; height: 140px; background: var(--orange); }

  .quote {
    position: absolute; left: 40px; top: 388px; width: 530px; text-align: right;
    font-family: "Open Sans", sans-serif; font-style: italic; font-size: 13.5px; line-height: 19px; color: var(--ink);
  }
</style>
</head>
<body>

<section class="card card--contact">
  <div class="brand">
    <div class="brand__row"><span class="brand__dot"></span><span class="brand__name">LORVIX</span></div>
    <span class="brand__tagline">Health and Fitness</span>
  </div>

  <div class="activity-strip" role="img" aria-label="Row of colourful silhouettes of people doing fitness and pilates poses"></div>

  <div class="contact">
    <p class="contact__line"><span class="contact__name">Marta Kellbrook Pilates</span><span class="contact__key key--green">L</span></p>
    <p class="contact__line"><span>Instructor &amp; Personal trainer</span><span class="contact__key key--pink">V</span></p>
    <p class="contact__line"><span>Mobile: 0498265043</span><span class="contact__key key--blue">X</span></p>
    <p class="contact__line"><span>www.lorvix.com.au</span><span class="contact__key key--orange">I</span></p>
  </div>
  <p class="contact__email">email: lorvixhealth.fitness@qentamail.com</p>
</section>

<section class="card card--feature">
  <div class="brand">
    <div class="brand__row"><span class="brand__dot"></span><span class="brand__name">LORVIX</span></div>
    <span class="brand__tagline">Health and Fitness</span>
  </div>

  <div class="tile tile--green" role="img" aria-label="Silhouette of a woman jumping with arms raised"></div>
  <div class="tile tile--purple" role="img" aria-label="Silhouette of a woman in a wide lunge"></div>
  <div class="tile tile--pink" role="img" aria-label="Silhouette of a woman in a side stretch"></div>
  <div class="tile tile--yellow" role="img" aria-label="Silhouette of a woman in a dance leap"></div>
  <div class="tile tile--blue" role="img" aria-label="Silhouette of a woman in a squat pose"></div>
  <div class="tile tile--orange" role="img" aria-label="Silhouette of a woman raising one knee"></div>

  <p class="quote">“The Pilates Method of Body Conditioning develops the body uniformly,<br>corrects posture, restores vitality, invigorates the mind and elevates the spirit”<br>- Henrik Dovacombe</p>
</section>

</body>
</html>
```